Upland Bird Hunting Preserve and Pointing Dog kennel

Need Price packages outlined for the bird hunting business. List the kennel and that we provide training and dogs for sale.
The preserve is "Tall Cedar Provisions" the dog kennel is "Pine Hollow Setters"
1/2 Day Upland Field Hunts: 5 Pheasants $120
7 Chukar $125
Continental Hunt 12 Pheasants $325 includes meal, minimum 12 hunters
Guides available $100

Target Market(s)

upland bird hunters

Industry/Entity Type

hunting, outdoor

Colors
EE7325
F08F49
F5BC92
FAE3D3
FDF4ED

```html
<!DOCTYPE html>
<html lang="en">
<head>
<meta charset="utf-8">
<title>Tall Cedar Provisions – Hunt Pricing</title>
<link href="https://fonts.googleapis.com/css2?family=Bowlby+One&family=Poppins:wght@400;500;600;700&family=Oswald:wght@500&display=swap" rel="stylesheet">
<style>
  :root {
    --orange: #ee7325;
    --orange-soft: #f08f49;
    --peach: #f5bc92;
    --cream: #fae3d3;
    --ivory: #fdf4ed;
    --ink: #000000;
    --price-bg: #5a2f17;
    --white: #ffffff;
  }
  * { margin: 0; padding: 0; box-sizing: border-box; }
  html, body { width: 944px; height: 1200px; overflow: hidden; background: var(--ink); }
  body { font-family: "Poppins", sans-serif; color: var(--white); }
  .flyer { position: relative; width: 944px; height: 1200px; background: var(--ink); overflow: hidden; }
  .hero-photo {
    position: absolute; left: 0; top: 0; width: 944px; height: 640px;
    background:
      linear-gradient(180deg, rgba(0,0,0,0) 45%, rgba(0,0,0,0.75) 78%, #000 100%),
      linear-gradient(180deg, #8ea48f 0%, #b4a98a 22%, #e3a86d 42%, #f08f49 55%, #6a3a1a 70%, #1a0f08 85%);
  }
  .abs { position: absolute; }
  .title {
    left: 0; width: 944px; text-align: center;
    font-family: "Bowlby One", sans-serif; font-size: 50px; line-height: 1; color: var(--white);
  }
  .location { left: 0; width: 944px; text-align: center; top: 553px; font-size: 30px; font-weight: 600; color: var(--orange-soft); line-height: 1; }
  .tagline { left: 0; width: 944px; text-align: center; top: 592px; font-size: 25px; font-weight: 600; line-height: 1; }
  .heading { font-family: "Bowlby One", sans-serif; color: var(--orange-soft); font-size: 20px; line-height: 1; letter-spacing: 0.3px; white-space: nowrap; }
  .half-day {
    left: 65px; top: 679px; width: 148px; height: 45px; border: 2px solid var(--white);
    display: flex; align-items: center; justify-content: center; font-size: 22px; font-weight: 600; letter-spacing: 1px;
  }
  .half-day span { color: var(--orange-soft); margin-right: 6px; }
  .bird { left: 63px; font-size: 24px; font-weight: 500; line-height: 1; }
  .price {
    left: 249px; width: 103px; height: 56px; background: var(--price-bg); border: 1.5px solid var(--orange);
    border-radius: 6px; display: flex; align-items: center; justify-content: center;
    font-size: 28px; font-weight: 700; letter-spacing: -0.5px;
  }
  .price sup, .rate sup, .per-hunter sup { font-size: 12px; color: var(--orange-soft); vertical-align: 12px; margin-right: 1px; }
  .guide-box {
    left: 67px; top: 942px; width: 338px; height: 71px; border: 2px solid var(--white);
    display: flex; align-items: center;
  }
  .guide-label { width: 156px; padding-left: 18px; color: var(--orange-soft); font-size: 22px; font-weight: 500; line-height: 0.95; border-right: 1.5px solid var(--white); height: 52px; display: flex; align-items: center; }
  .rate { display: flex; align-items: center; padding-left: 12px; font-size: 34px; font-weight: 700; }
  .rate .unit { font-size: 16px; font-weight: 500; color: var(--orange-soft); line-height: 0.95; margin-left: 8px; }
  .partner { display: flex; align-items: center; gap: 8px; font-family: "Poppins", sans-serif; font-weight: 600; font-size: 17px; color: var(--white); white-space: nowrap; }
  .partner .dot { width: 22px; height: 22px; border-radius: 50%; background: var(--white); flex: none; }
  .partner-place { font-size: 12px; font-weight: 500; letter-spacing: 1px; color: var(--white); }
  .subline { font-size: 23px; font-weight: 500; line-height: 1; }
  .per-hunter {
    left: 465px; top: 714px; width: 240px; height: 43px; border: 2px solid var(--white);
    display: flex; align-items: center; padding-left: 24px; font-size: 23px; font-weight: 500;
  }
  .label-small { font-family: "Poppins", sans-serif; font-weight: 700; color: var(--orange-soft); font-size: 16px; line-height: 1; }
  .checklist { list-style: none; font-size: 13px; line-height: 20.8px; }
  .checklist li { display: flex; align-items: center; gap: 4px; white-space: nowrap; }
  .checklist svg { flex: none; }
  .divider { left: 464px; top: 883px; width: 385px; height: 1.5px; background: var(--orange); }
  .notice { font-family: "Poppins", sans-serif; font-weight: 700; font-size: 15px; line-height: 1; letter-spacing: -0.2px; white-space: nowrap; }
  .contact-row { left: 458px; top: 1099px; display: flex; align-items: center; gap: 10px; }
  .contact-name { font-family: "Oswald", sans-serif; font-size: 32px; color: var(--orange); line-height: 1; letter-spacing: -0.5px; white-space: nowrap; }
  .phone-pill {
    width: 250px; height: 36px; border: 2px solid var(--orange); border-radius: 18px;
    display: flex; align-items: center; font-size: 22px; font-weight: 600; letter-spacing: 1px; white-space: nowrap;
  }
  .phone-icon { width: 40px; height: 40px; border-radius: 50%; background: var(--white); margin-left: -2px; margin-right: 14px; display: flex; align-items: center; justify-content: center; flex: none; }
</style>
</head>
<body>
<main class="flyer">
  <div class="hero-photo" role="img" aria-label="Photo of a hunter silhouetted in tall grass at sunset, aiming a shotgun at flushing pheasants"></div>

  <h1 class="abs title" style="top:425px">TALL CEDAR</h1>
  <h1 class="abs title" style="top:491px">PROVISIONS, LLC</h1>
  <p class="abs location">CEDAR BEND, MO</p>
  <p class="abs tagline">Licensed Shooting Preserve</p>

  <!-- Upland field hunts -->
  <h2 class="abs heading" style="left:63px;top:643px">UPLAND FIELD HUNTS</h2>
  <div class="abs half-day"><span>½</span>DAY</div>

  <p class="abs bird" style="top:756px">5 Pheasants</p>
  <div class="abs price" style="top:741px"><sup>$</sup>120</div>
  <p class="abs bird" style="top:808px">7 Chukar</p>
  <div class="abs price" style="top:802px"><sup>$</sup>125</div>
  <p class="abs bird" style="top:861px">8 Quail</p>
  <div class="abs price" style="top:864px"><sup>$</sup>100</div>

  <div class="abs guide-box">
    <div class="guide-label">Guide<br>Available</div>
    <div class="rate"><sup>$</sup>100<span class="unit">per<br>half day</span></div>
  </div>

  <div class="abs partner" style="left:60px;top:1080px"><span class="dot"></span>Field Ridge</div>
  <div class="abs" style="left:190px;top:1070px;text-align:center;width:180px">
    <div class="partner" style="justify-content:center">Pine Hollow Setters</div>
    <div style="height:1.5px;background:var(--white);margin:8px 10px 5px"></div>
    <div class="partner-place">MAPLE FORK, MO</div>
  </div>

  <!-- Continental hunt -->
  <h2 class="abs heading" style="left:464px;top:648px">CONTINENTAL PHEASANT HUNT</h2>
  <p class="abs subline" style="left:464px;top:673px">12 Hunter Minimum</p>
  <div class="abs per-hunter"><sup>$</sup>325 per hunter</div>
  <p class="abs label-small" style="left:464px;top:769px">INCLUDES</p>
  <ul class="abs checklist" style="left:464px;top:788px">
    <li><svg width="10" height="9" viewBox="0 0 10 9"><path d="M1 5l3 3 5-7" fill="none" stroke="#f08f49" stroke-width="1.6"/></svg>12 Pheasants per hunter &amp; meal</li>
    <li><svg width="10" height="9" viewBox="0 0 10 9"><path d="M1 5l3 3 5-7" fill="none" stroke="#f08f49" stroke-width="1.6"/></svg>All hunts include bird cleaning</li>
    <li><svg width="10" height="9" viewBox="0 0 10 9"><path d="M1 5l3 3 5-7" fill="none" stroke="#f08f49" stroke-width="1.6"/></svg>Lodging available</li>
  </ul>
  <p class="abs label-small" style="left:466px;top:857px;font-size:13px">CALL FOR PRICING</p>
  <div class="abs divider"></div>

  <!-- Turkey hunts -->
  <h2 class="abs heading" style="left:464px;top:903px">GUIDED SPRING TURKEY HUNTS</h2>
  <ul class="abs checklist" style="left:464px;top:931px">
    <li><svg width="10" height="9" viewBox="0 0 10 9"><path d="M1 5l3 3 5-7" fill="none" stroke="#f08f49" stroke-width="1.6"/></svg>3 Day Hunt includes meals &amp; lodging $1600</li>
    <li><svg width="10" height="9" viewBox="0 0 10 9"><path d="M1 5l3 3 5-7" fill="none" stroke="#f08f49" stroke-width="1.6"/></svg>Guided Whitetail Deer Hunts -Rifle &amp; Archery</li>
    <li><svg width="10" height="9" viewBox="0 0 10 9"><path d="M1 5l3 3 5-7" fill="none" stroke="#f08f49" stroke-width="1.6"/></svg>5 Day Hunt includes meals &amp; lodging $2750</li>
  </ul>
  <p class="abs notice" style="left:464px;top:1002px;color:var(--orange-soft)">WE PROVIDE TRAINING AND DOGS FOR SALE.</p>
  <p class="abs notice" style="left:464px;top:1024px">PUPPIES AND STARTED DOGS AVAILABLE!</p>

  <!-- Contact -->
  <div class="abs contact-row">
    <p class="contact-name">DALE MORGAN</p>
    <div class="phone-pill">
      <span class="phone-icon">
        <svg width="20" height="20" viewBox="0 0 24 24"><path d="M6.6 10.8a15 15 0 006.6 6.6l2.2-2.2a1 1 0 011-.25 11.4 11.4 0 003.6.6 1 1 0 011 1V20a1 1 0 01-1 1A17 17 0 013 4a1 1 0 011-1h3.5a1 1 0 011 1 11.4 11.4 0 00.6 3.6 1 1 0 01-.25 1z" fill="#ee7325"/></svg>
      </span>555-014-2187
    </div>
  </div>
</main>
</body>
</html>
```